Bright Harbor need a basic Calendar design

Our customers like when we give them a calendar every year but we have undergone some changes in our branding and we seek a similar product to what we delivered, but with new logos and a fresh look. If you can incorporate some stock imagery or something that is fine (like the attached apples but not necessarily that image, thats fine). This is a basic corporate calendar,

See attached photos for what we are looking for. Essentially the same exact type of wall calendar with new logo and images. That is all.

Industry/Entity Type

Product

Font styles to use
Serif
Sans Serif

Colors
3277b5
0355a3
85abd2
ffffff

```html
<!DOCTYPE html>
<html lang="en">
<head>
<meta charset="utf-8">
<title>Bright Harbor 2015 Wall Calendar</title>
<link rel="stylesheet" href="https://fonts.googleapis.com/css2?family=Montserrat:wght@500;600;700;800&display=swap">
<style>
  :root {
    --brand-blue: #1d5ad8;
    --deep-blue: #0355a3;
    --mid-blue: #3277b5;
    --grid-line: #85abd2;
    --paper: #ffffff;
    --ink: #1d2a3a;
    --sky-top: #8fa9bf;
    --sky-low: #c9d6de;
    --hills: #4d5e63;
    --lake: #3f6f8e;
    --lake-deep: #2b5470;
  }
  * { box-sizing: border-box; margin: 0; padding: 0; }
  html, body { width: 700px; height: 1200px; overflow: hidden; background: var(--paper); }
  body { font-family: "Montserrat", sans-serif; color: var(--ink); }

  .calendar { position: relative; width: 700px; height: 1200px; background: var(--paper); }

  .hero {
    position: absolute; left: 0; top: 0; width: 700px; height: 168px;
    background:
      linear-gradient(180deg, var(--sky-top) 0%, var(--sky-low) 30%, var(--hills) 40%, var(--lake) 48%, var(--lake-deep) 100%);
  }
  .brand-name {
    position: absolute; top: 44px; left: 0; width: 700px; text-align: center;
    font-weight: 700; font-size: 22px; letter-spacing: 1px; color: var(--paper);
  }
  .year {
    position: absolute; right: 56px; top: 138px;
    font-weight: 800; font-size: 30px; line-height: 1; color: var(--paper);
  }

  .month { position: absolute; width: 189px; }
  .month-name {
    height: 28px; line-height: 28px; text-align: center;
    background: var(--brand-blue); color: var(--paper);
    font-weight: 600; font-size: 17px; letter-spacing: 0.3px;
  }
  .days {
    margin-top: 3px; height: 196px;
    display: grid; grid-template-columns: repeat(7, 1fr); grid-template-rows: repeat(5, 1fr);
    gap: 2px; padding: 2px; background: var(--grid-line);
  }
  .days > span {
    position: relative; background: var(--paper);
    font-size: 6.5px; font-weight: 600; padding: 3px 0 0 4px; line-height: 1;
  }
  .days > .split em {
    font-style: normal; display: block;
  }
  .days > .split em + em {
    position: absolute; left: 0; right: 0; bottom: 0; height: 14px;
    border-top: 2px solid var(--grid-line); padding: 3px 0 0 4px;
  }

  .col-1 { left: 56px; } .col-2 { left: 256px; } .col-3 { left: 455px; }
  .row-1 { top: 183px; } .row-2 { top: 434px; } .row-3 { top: 683px; } .row-4 { top: 934px; }
</style>
</head>
<body>
<main class="calendar">
  <header class="hero" role="img" aria-label="Lake photograph with a lone tree standing in the water and mountains beyond">
    <div class="brand-name">Bright Harbor</div>
    <div class="year">2015</div>
  </header>

  <section class="month col-1 row-1"><h2 class="month-name">JANUARY</h2><div class="days">
    <span></span><span></span><span></span><span></span><span>1</span><span>2</span><span>3</span>
    <span>4</span><span>5</span><span>6</span><span>7</span><span>8</span><span>9</span><span>10</span>
    <span>11</span><span>12</span><span>13</span><span>14</span><span>15</span><span>16</span><span>17</span>
    <span>18</span><span>19</span><span>20</span><span>21</span><span>22</span><span>23</span><span>24</span>
    <span>25</span><span>26</span><span>27</span><span>28</span><span>29</span><span>30</span><span>31</span>
  </div></section>

  <section class="month col-2 row-1"><h2 class="month-name">FEBRUARY</h2><div class="days">
    <span>1</span><span>2</span><span>3</span><span>4</span><span>5</span><span>6</span><span>7</span>
    <span>8</span><span>9</span><span>10</span><span>11</span><span>12</span><span>13</span><span>14</span>
    <span>15</span><span>16</span><span>17</span><span>18</span><span>19</span><span>20</span><span>21</span>
    <span>22</span><span>23</span><span>24</span><span>25</span><span>26</span><span>27</span><span>28</span>
    <span></span><span></span><span></span><span></span><span></span><span></span><span></span>
  </div></section>

  <section class="month col-3 row-1"><h2 class="month-name">MARCH</h2><div class="days">
    <span>1</span><span>2</span><span>3</span><span>4</span><span>5</span><span>6</span><span>7</span>
    <span>8</span><span>9</span><span>10</span><span>11</span><span>12</span><span>13</span><span>14</span>
    <span>15</span><span>16</span><span>17</span><span>18</span><span>19</span><span>20</span><span>21</span>
    <span>22</span><span>23</span><span>24</span><span>25</span><span>26</span><span>27</span><span>28</span>
    <span>29</span><span>30</span><span>31</span><span></span><span></span><span></span><span></span>
  </div></section>

  <section class="month col-1 row-2"><h2 class="month-name">APRIL</h2><div class="days">
    <span></span><span></span><span></span><span>1</span><span>2</span><span>3</span><span>4</span>
    <span>5</span><span>6</span><span>7</span><span>8</span><span>9</span><span>10</span><span>11</span>
    <span>12</span><span>13</span><span>14</span><span>15</span><span>16</span><span>17</span><span>18</span>
    <span>19</span><span>20</span><span>21</span><span>22</span><span>23</span><span>24</span><span>25</span>
    <span>26</span><span>27</span><span>28</span><span>29</span><span>30</span><span></span><span></span>
  </div></section>

  <section class="month col-2 row-2"><h2 class="month-name">MAY</h2><div class="days">
    <span></span><span></span><span></span><span></span><span></span><span>1</span><span>2</span>
    <span>3</span><span>4</span><span>5</span><span>6</span><span>7</span><span>8</span><span>9</span>
    <span>10</span><span>11</span><span>12</span><span>13</span><span>14</span><span>15</span><span>16</span>
    <span>17</span><span>18</span><span>19</span><span>20</span><span>21</span><span>22</span><span>23</span>
    <span class="split"><em>24</em><em>31</em></span><span>25</span><span>26</span><span>27</span><span>28</span><span>29</span><span>30</span>
  </div></section>

  <section class="month col-3 row-2"><h2 class="month-name">JUNE</h2><div class="days">
    <span></span><span>1</span><span>2</span><span>3</span><span>4</span><span>5</span><span>6</span>
    <span>7</span><span>8</span><span>9</span><span>10</span><span>11</span><span>12</span><span>13</span>
    <span>14</span><span>15</span><span>16</span><span>17</span><span>18</span><span>19</span><span>20</span>
    <span>21</span><span>22</span><span>23</span><span>24</span><span>25</span><span>26</span><span>27</span>
    <span>28</span><span>29</span><span>30</span><span></span><span></span><span></span><span></span>
  </div></section>

  <section class="month col-1 row-3"><h2 class="month-name">JULY</h2><div class="days">
    <span></span><span></span><span></span><span>1</span><span>2</span><span>3</span><span>4</span>
    <span>5</span><span>6</span><span>7</span><span>8</span><span>9</span><span>10</span><span>11</span>
    <span>12</span><span>13</span><span>14</span><span>15</span><span>16</span><span>17</span><span>18</span>
    <span>19</span><span>20</span><span>21</span><span>22</span><span>23</span><span>24</span><span>25</span>
    <span>26</span><span>27</span><span>28</span><span>29</span><span>30</span><span>31</span><span></span>
  </div></section>

  <section class="month col-2 row-3"><h2 class="month-name">AUGUST</h2><div class="days">
    <span></span><span></span><span></span><span></span><span></span><span></span><span>1</span>
    <span>2</span><span>3</span><span>4</span><span>5</span><span>6</span><span>7</span><span>8</span>
    <span>9</span><span>10</span><span>11</span><span>12</span><span>13</span><span>14</span><span>15</span>
    <span>16</span><span>17</span><span>18</span><span>19</span><span>20</span><span>21</span><span>22</span>
    <span class="split"><em>23</em><em>30</em></span><span class="split"><em>24</em><em>31</em></span><span>25</span><span>26</span><span>27</span><span>28</span><span>29</span>
  </div></section>

  <section class="month col-3 row-3"><h2 class="month-name">SEPTEMBER</h2><div class="days">
    <span></span><span></span><span>1</span><span>2</span><span>3</span><span>4</span><span>5</span>
    <span>6</span><span>7</span><span>8</span><span>9</span><span>10</span><span>11</span><span>12</span>
    <span>13</span><span>14</span><span>15</span><span>16</span><span>17</span><span>18</span><span>19</span>
    <span>20</span><span>21</span><span>22</span><span>23</span><span>24</span><span>25</span><span>26</span>
    <span>27</span><span>28</span><span>29</span><span>30</span><span></span><span></span><span></span>
  </div></section>

  <section class="month col-1 row-4"><h2 class="month-name">OCTOBER</h2><div class="days">
    <span></span><span></span><span></span><span></span><span>1</span><span>2</span><span>3</span>
    <span>4</span><span>5</span><span>6</span><span>7</span><span>8</span><span>9</span><span>10</span>
    <span>11</span><span>12</span><span>13</span><span>14</span><span>15</span><span>16</span><span>17</span>
    <span>18</span><span>19</span><span>20</span><span>21</span><span>22</span><span>23</span><span>24</span>
    <span>25</span><span>26</span><span>27</span><span>28</span><span>29</span><span>30</span><span>31</span>
  </div></section>

  <section class="month col-2 row-4"><h2 class="month-name">NOVEMBER</h2><div class="days">
    <span>1</span><span>2</span><span>3</span><span>4</span><span>5</span><span>6</span><span>7</span>
    <span>8</span><span>9</span><span>10</span><span>11</span><span>12</span><span>13</span><span>14</span>
    <span>15</span><span>16</span><span>17</span><span>18</span><span>19</span><span>20</span><span>21</span>
    <span>22</span><span>23</span><span>24</span><span>25</span><span>26</span><span>27</span><span>28</span>
    <span>29</span><span>30</span><span></span><span></span><span></span><span></span><span></span>
  </div></section>

  <section class="month col-3 row-4"><h2 class="month-name">DECEMBER</h2><div class="days">
    <span></span><span></span><span>1</span><span>2</span><span>3</span><span>4</span><span>5</span>
    <span>6</span><span>7</span><span>8</span><span>9</span><span>10</span><span>11</span><span>12</span>
    <span>13</span><span>14</span><span>15</span><span>16</span><span>17</span><span>18</span><span>19</span>
    <span>20</span><span>21</span><span>22</span><span>23</span><span>24</span><span>25</span><span>26</span>
    <span>27</span><span>28</span><span>29</span><span>30</span><span>31</span><span></span><span></span>
  </div></section>
</main>
</body>
</html>
```